Business Card for Managing Partner Investment Fund

To create a business card template for an investment fund manager. Business card should be more professional in nature, not too colorful, more upscale, and created using the attached logos and fund name files. I would prefer a black or gray color scheme, but am open to the use of color as well. I would prefer a double sided business card, but open to single sided business card designs as well. The business card should include: name, title, and contact information, as well as logo and company name. I would prefer a more stream-lined, simple business card design.
Updates
Address: 4190 NE 38th Ter. Ocala, FL 34470
Email: talvin47@quorimail.net
Phone: 561-347-9162
Title: managing partner
Name: Dorian Velsky
Fund Name: Ambergate Capital
Logos can be found in files attached to the brief
Target Market(s)
potential investors, other fund managers
Industry/Entity Type
Finance
Contact Information for Business Card
Name on card: Dorian Velsky
Title: Managing Partner
Colors
Designer to choose colors to be used in the design.
Requirements
Must have
- Phone number
- email address
- physical address
- title
- name
- logo
- Fund name
Nice to have
- simple layout
Should not have
- too many colors, busy fonts,

```html
<!DOCTYPE html>
<html lang="en">
<head>
<meta charset="UTF-8">
<title>Ambergate Capital – Business Card</title>
<link href="https://fonts.googleapis.com/css2?family=Open+Sans:wght@400;600;700&display=swap" rel="stylesheet">
<style>
  :root {
    --page-bg: #e9e7e4;
    --card-black: #1f1f1f;
    --card-white: #ffffff;
    --ink: #1a1a1a;
    --ink-soft: #555555;
    --grey-mark: #4a4a4a;
    --rule: #4a4a4a;
    --accent-bar: #6e6e6e;
  }
  * { box-sizing: border-box; margin: 0; padding: 0; }
  html, body {
    width: 1200px; height: 800px; overflow: hidden;
    background: var(--page-bg);
    font-family: "Open Sans", Arial, sans-serif;
  }
  .stage {
    width: 1200px; height: 800px;
    display: flex; align-items: center; justify-content: center; gap: 40px;
  }
  .card {
    width: 560px; height: 320px;
    border-radius: 18px;
    position: relative;
    overflow: hidden;
    box-shadow: 0 6px 18px rgba(0,0,0,0.18);
  }
  /* Front */
  .card-front {
    background: var(--card-black);
    display: flex; align-items: center; justify-content: center;
  }
  .front-name {
    color: var(--grey-mark);
    font-weight: 600;
    font-size: 34px;
    letter-spacing: 4px;
    text-transform: uppercase;
  }
  /* Back */
  .card-back { background: var(--card-white); color: var(--ink); }
  .back-brand {
    position: absolute; top: 40px; right: 40px;
    font-weight: 600; font-size: 22px; letter-spacing: 2.5px;
    text-transform: uppercase; color: var(--ink);
  }
  .web-line {
    position: absolute; right: 40px; top: 90px;
    display: flex; align-items: center; gap: 12px;
    width: 320px;
  }
  .web-line .rule { flex: 1; height: 1.5px; background: var(--rule); }
  .web-line .web { font-size: 11px; color: var(--ink-soft); }
  .identity {
    position: absolute; left: 0; top: 126px;
    padding-left: 34px;
    border-left: 14px solid var(--accent-bar);
  }
  .person-name { font-size: 24px; font-weight: 400; line-height: 1.1; }
  .person-name strong { font-weight: 700; }
  .person-title { font-size: 12.5px; color: var(--ink-soft); margin-top: 3px; }
  .contacts {
    position: absolute; left: 48px; bottom: 34px;
    list-style: none; font-size: 12.5px; color: var(--ink);
  }
  .contacts li { display: flex; align-items: flex-start; gap: 9px; margin-top: 5px; line-height: 1.3; }
  .contacts svg { width: 12px; height: 12px; flex: none; margin-top: 2px; fill: var(--ink-soft); }
</style>
</head>
<body>
<main class="stage">
  <section class="card card-front" aria-label="Card front">
    <span class="front-name">Ambergate Capital</span>
  </section>

  <section class="card card-back" aria-label="Card back">
    <div class="back-brand">Ambergate Capital</div>
    <div class="web-line"><span class="rule"></span><span class="web">www.ambergatecap.example</span></div>

    <div class="identity">
      <p class="person-name">Dorian <strong>Velsky</strong></p>
      <p class="person-title">Managing Partner</p>
    </div>

    <ul class="contacts">
      <li>
        <svg viewBox="0 0 24 24" aria-hidden="true"><path d="M6.6 10.8a15 15 0 0 0 6.6 6.6l2.2-2.2c.3-.3.7-.4 1-.2 1.1.4 2.3.6 3.6.6.6 0 1 .4 1 1V20c0 .6-.4 1-1 1A17 17 0 0 1 3 4c0-.6.4-1 1-1h3.5c.6 0 1 .4 1 1 0 1.3.2 2.5.6 3.6.1.3 0 .7-.2 1z"/></svg>
        <span>561-555-0147</span>
      </li>
      <li>
        <svg viewBox="0 0 24 24" aria-hidden="true"><path d="M2 5h20v14H2z M2 5l10 8 10-8"/></svg>
        <span>talvin47@quorimail.net</span>
      </li>
      <li>
        <svg viewBox="0 0 24 24" aria-hidden="true"><path d="M12 2a7 7 0 0 0-7 7c0 5 7 13 7 13s7-8 7-13a7 7 0 0 0-7-7zm0 9.5A2.5 2.5 0 1 1 12 6.5a2.5 2.5 0 0 1 0 5z"/></svg>
        <span>4190 Quillmere Ter.<br>Ocala, FL 34470</span>
      </li>
    </ul>
  </section>
</main>
</body>
</html>
```